Lending Harbor Partners - business cards

we need new business cards for my company.
i've been in business for 25 years.
my wife and I are mortgage brokers.

we just bought the domain for a website with www.bluekeyhomes.example
that could be used in the design also.

On the business card would be
Front card:

Dale Whitcombe
Owner/Loan Officer
Cell: (555) 814-2976
Lending Harbor Partners
4237 Maple Crest Lane
Santa Clarita, CA 90000
Office (555) 430-7152
Fax (555) 430-7159
website www.bluekeyhomes.example

Back of Card:

LHP BRE #0873512 NMLS #528946
Dale Whitcombe BRE # 06739481 NMLS #527314

```html
<!DOCTYPE html>
<html lang="en">
<head>
<meta charset="utf-8">
<title>Lending Harbor Partners – Business Cards</title>
<link rel="stylesheet" href="https://fonts.googleapis.com/css2?family=Open+Sans:wght@400;600;700&display=swap">
<style>
  :root {
    --page-bg: #e4e4e4;
    --brown: #5a322c;
    --brown-text: #b79a92;
    --sky: #17a6e1;
    --ink: #1b2a3a;
    --ink-soft: #24455e;
    --navy: #1d3f86;
    --white: #ffffff;
  }
  * { box-sizing: border-box; margin: 0; padding: 0; }
  html, body {
    width: 1200px; height: 1200px; overflow: hidden;
    background: var(--page-bg);
    font-family: "Open Sans", Arial, sans-serif;
  }
  .sheet {
    width: 1200px; height: 1200px;
    display: flex; flex-direction: column; align-items: center; justify-content: center;
    gap: 60px;
  }
  .card {
    position: relative;
    width: 700px; height: 400px;
    box-shadow: 0 6px 18px rgba(0,0,0,0.18);
    overflow: hidden;
  }

  /* Back side */
  .card--back { background: var(--brown); }
  .card--back .brand {
    position: absolute; left: 250px; top: 118px;
  }
  .brand {
    display: flex; align-items: center; gap: 16px;
  }
  .brand__dot {
    width: 44px; height: 44px; border-radius: 50%;
    background: var(--navy); flex: none;
  }
  .brand__name {
    color: var(--white); font-weight: 700; font-size: 30px; line-height: 1.05;
  }
  .licenses {
    position: absolute; left: 310px; top: 218px;
    color: var(--brown-text); font-size: 16px; line-height: 1.4;
  }

  /* Front side */
  .card--front { background: var(--sky); }
  .tab {
    position: absolute; width: 18px; height: 48px; background: var(--brown);
  }
  .tab--left-top { left: 118px; top: 0; }
  .tab--left-bottom { left: 50px; bottom: 0; }
  .tab--right { right: 0; top: 210px; height: 70px; }
  .contact {
    position: absolute; left: 70px; top: 70px;
    color: var(--ink-soft); font-size: 17px; line-height: 1.4;
  }
  .contact__name { color: var(--ink); font-weight: 700; font-size: 21px; }
  .contact__group { margin-top: 14px; }
  .contact__line { display: flex; align-items: center; gap: 8px; }
  .icon {
    width: 16px; height: 16px; flex: none;
  }
  .card--front .brand {
    position: absolute; left: 400px; top: 150px;
  }
  .card--front .brand__name { font-size: 26px; }
</style>
</head>
<body>
<main class="sheet">

  <section class="card card--back" aria-label="Business card back">
    <div class="brand">
      <span class="brand__dot"></span>
      <span class="brand__name">Lending Harbor<br>Partners</span>
    </div>
    <div class="licenses">
      <p>LHP BRE #0873512</p>
      <p>NMLS #528946</p>
      <p>Dale Whitcombe BRE # 06739481</p>
      <p>NMLS #527314</p>
    </div>
  </section>

  <section class="card card--front" aria-label="Business card front">
    <span class="tab tab--left-top"></span>
    <span class="tab tab--left-bottom"></span>
    <span class="tab tab--right"></span>

    <div class="contact">
      <p class="contact__name">Dale Whitcombe</p>
      <p>Owner/Loan Officer</p>
      <p class="contact__line">
        <svg class="icon" viewBox="0 0 16 16" aria-hidden="true"><rect x="1" y="1" width="14" height="14" rx="2" fill="#5a322c"/><rect x="5" y="3" width="6" height="10" rx="1" fill="#e9d8c9"/></svg>
        (555) 814-2976
      </p>
      <div class="contact__group">
        <p>4237 Maple Crest Lane</p>
        <p>Santa Clarita, CA 90000</p>
      </div>
      <div class="contact__group">
        <p class="contact__line">
          <svg class="icon" viewBox="0 0 16 16" aria-hidden="true"><rect x="1" y="1" width="14" height="14" rx="2" fill="#5a322c"/><path d="M4 5h8v6H4z" fill="#e9d8c9"/></svg>
          (555) 430-7152
        </p>
        <p class="contact__line">
          <svg class="icon" viewBox="0 0 16 16" aria-hidden="true"><rect x="1" y="1" width="14" height="14" rx="2" fill="#5a322c"/><path d="M4 7h8v5H4zM6 4h4v3H6z" fill="#e9d8c9"/></svg>
          (555) 430-7159
        </p>
        <p class="contact__line">
          <svg class="icon" viewBox="0 0 16 16" aria-hidden="true"><circle cx="8" cy="8" r="7" fill="#5a322c"/><circle cx="8" cy="8" r="4.5" fill="none" stroke="#e9d8c9" stroke-width="1.2"/><path d="M3.5 8h9M8 3.5v9" stroke="#e9d8c9" stroke-width="1"/></svg>
          www.bluekeyhomes.example
        </p>
      </div>
    </div>

    <div class="brand">
      <span class="brand__dot"></span>
      <span class="brand__name">Lending Harbor<br>Partners</span>
    </div>
  </section>

</main>
</body>
</html>
```